New Business Card Design Project

We want a modern business card that catches the attention of other remodeling companies as well as homeowners. We would like it to be informative but still simple.

Target Market(s)

Residential and other Business's

Contact Information for Business Card

TrellBrix
Phone number is 5550192748
Address is
4817 SW 3rd Lane
Larkfield, Ohmara 60418
email is trellbrixco@quamlet.com

Requirements
Must have
• Our tagline
• Trusted · Skilled · Fairly Priced

```html
<!DOCTYPE html>
<html lang="en">
<head>
<meta charset="utf-8">
<title>TrellBrix Business Card</title>
<link rel="stylesheet" href="https://fonts.googleapis.com/css2?family=Saira+Condensed:wght@600;700&family=Roboto:wght@400;500&display=swap">
<style>
  :root {
    --brand-blue: #1662be;
    --brand-orange: #c5500f;
    --card-paper: #f3f3f2;
    --page-bg: #b9b9b9;
    --ink: #2b2b2b;
  }
  * { margin: 0; padding: 0; box-sizing: border-box; }
  html, body { width: 1200px; height: 576px; overflow: hidden; }
  body { background: var(--page-bg); position: relative; font-family: "Roboto", sans-serif; color: var(--ink); }

  .card {
    position: absolute;
    background: var(--card-paper);
    border-radius: 9px;
    overflow: hidden;
    box-shadow: 0 3px 6px rgba(0,0,0,0.25);
  }
  .card--front { left: 82px; top: 139px; width: 484px; height: 293px; }
  .card--back  { left: 602px; top: 138px; width: 480px; height: 291px; }

  .wordmark {
    position: absolute;
    display: flex;
    align-items: center;
    gap: 10px;
    font-family: "Saira Condensed", sans-serif;
    font-weight: 700;
    color: var(--brand-blue);
    letter-spacing: 1px;
    line-height: 1;
    text-transform: uppercase;
    white-space: nowrap;
  }
  .wordmark__dot { border-radius: 50%; background: var(--brand-orange); flex: none; }

  .tagline {
    position: absolute;
    font-family: "Roboto", sans-serif;
    font-weight: 500;
    color: var(--ink);
    letter-spacing: 1.5px;
    text-transform: uppercase;
    white-space: nowrap;
    line-height: 1;
  }

  /* Front */
  .card--front .wordmark { left: 0; right: 0; top: 98px; justify-content: center; font-size: 62px; }
  .card--front .wordmark__dot { width: 18px; height: 18px; }
  .card--front .tagline { left: 0; right: 0; top: 166px; text-align: center; font-size: 13px; }
  .front-url {
    position: absolute; left: 0; right: 0; top: 257px;
    display: flex; justify-content: center; align-items: center; gap: 18px;
    font-size: 13px; color: #3a3a3a;
  }
  .front-url .dash { width: 32px; height: 2px; background: var(--brand-blue); border-radius: 2px; }
  .front-band { position: absolute; left: 0; right: 0; bottom: 0; height: 12px; display: flex; }
  .front-band span { flex: 1; }
  .front-band .blue { background: var(--brand-blue); }
  .front-band .orange { background: var(--brand-orange); }

  /* Back */
  .card--back .wordmark { right: 28px; top: 48px; font-size: 46px; }
  .card--back .wordmark__dot { width: 13px; height: 13px; }
  .card--back .tagline { right: 28px; top: 101px; font-size: 10.5px; }
  .holder-name {
    position: absolute; left: 29px; top: 154px;
    font-family: "Saira Condensed", sans-serif; font-weight: 600;
    font-size: 20px; color: var(--brand-orange); line-height: 1;
  }
  .holder-role { position: absolute; left: 29px; top: 180px; font-size: 12.5px; color: #333; }
  .role-rule { position: absolute; left: 146px; right: 28px; top: 187px; height: 1.5px; background: var(--brand-blue); }
  .contact-list { position: absolute; left: 29px; top: 216px; list-style: none; }
  .contact-list li { display: flex; align-items: center; gap: 10px; height: 18px; font-size: 12.5px; }
  .contact-list svg { width: 12px; height: 12px; fill: var(--brand-orange); flex: none; }
  .address { position: absolute; right: 28px; top: 234px; text-align: right; font-size: 12.5px; line-height: 18px; }
</style>
</head>
<body>
  <section class="card card--front">
    <div class="wordmark"><span class="wordmark__dot"></span>TrellBrix</div>
    <p class="tagline">Trusted · Skilled · Fairly Priced</p>
    <p class="front-url"><span class="dash"></span>www.trellbrix.com<span class="dash"></span></p>
    <div class="front-band"><span class="blue"></span><span class="orange"></span></div>
  </section>

  <section class="card card--back">
    <div class="wordmark"><span class="wordmark__dot"></span>TrellBrix</div>
    <p class="tagline">Trusted · Skilled · Fairly Priced</p>
    <p class="holder-name">Jane Roe Carter</p>
    <p class="holder-role">Managing Director</p>
    <div class="role-rule"></div>
    <ul class="contact-list">
      <li>
        <svg viewBox="0 0 12 12" aria-hidden="true"><path d="M1 4.5C1 2.5 3 1.5 6 1.5S11 2.5 11 4.5L9 5 8.5 3.8h-5L3 5zM3.5 5.5h5l1.5 5H2z"/></svg>
        5550192748
      </li>
      <li>
        <svg viewBox="0 0 12 12" aria-hidden="true"><path d="M1 2.5h10v7H1zM1.8 3.2 6 6.5l4.2-3.3" stroke="#f3f3f2" stroke-width="0.9"/></svg>
        trellbrixco@quamlet.com
      </li>
      <li>
        <svg viewBox="0 0 12 12" aria-hidden="true"><circle cx="6" cy="6" r="5"/><path d="M1 6h10M6 1c-2.4 2.8-2.4 7.2 0 10M6 1c2.4 2.8 2.4 7.2 0 10" stroke="#f3f3f2" stroke-width="0.8" fill="none"/></svg>
        www.trellbrix.com
      </li>
    </ul>
    <p class="address">4817 SW 3rd Lane<br>Larkfield, Ohmara 60418</p>
  </section>
</body>
</html>
```